Bref créative
Business Card Design for Law Firm
Harlow Legal Partners
Professional
Derek M. Falbo
Trial Lawyer
2730 Birchwood Avenue
North Annex - Suite 2100
Philadelphia, PA 19102
555-014-2737 (use as place holder)
derek@harlowcounsel.example
www.harlowcounsel.example
I am looking for a bold logo and business card design for a start-up law firm based in Philadelphia and with offices in PA and NJ. Harlow Legal Partners is led by trial attorneys and specializes in catastrophic personal injury litigation stemming from construction / industrial accidents, truck/auto accidents, defective products, falls, and medical malpractice.
New #s for phone and fax will be supplied upon selection of winning design.
Areas of Expertise:
- Personal Injury
- Wrongful Death
- Construction Accidents
- Work Injuries
- Car & Truck Accidents
- Motorcycle Accidents
- Medical Malpractice
- Nursing Home Abuse
- Premises Liability
- Longshore / Maritime
- Commercial Litigation
White Version
Black Version

```html
<!DOCTYPE html>
<html lang="en">
<head>
<meta charset="utf-8">
<title>Harlow Legal Partners – Stationery</title>
<link href="https://fonts.googleapis.com/css2?family=Raleway:wght@400;600&display=swap" rel="stylesheet">
<style>
:root{
  --bg-top:#f4f4f4;
  --bg-bottom:#cfcfcf;
  --paper:#ffffff;
  --blue:#1d6fc4;
  --blue-dark:#0c4a93;
  --blue-light:#5fb0ec;
  --ink:#4a4f57;
  --muted:#9aa0a8;
}
*{box-sizing:border-box;margin:0;padding:0}
html,body{width:1200px;height:247px;overflow:hidden}
body{
  position:relative;
  background:linear-gradient(var(--bg-top),var(--bg-bottom));
  font-family:"Raleway",sans-serif;color:var(--ink);
}
.piece{position:absolute;background:var(--paper);box-shadow:0 1px 3px rgba(0,0,0,.25);overflow:hidden}
.brand{display:flex;align-items:center;gap:3px;font-weight:600;color:var(--blue);white-space:nowrap}
.brand .dot{border-radius:50%;background:var(--blue);flex:none}
.brand.light{color:#fff}
.brand.light .dot{background:#fff}

/* intro logo */
.intro{position:absolute;left:8px;top:30px}
.intro .brand{font-size:10px}
.intro .brand .dot{width:14px;height:14px}
.intro .label{font-size:5px;color:var(--muted);margin-top:26px}

/* business cards */
.card{width:58px;height:33px}
.card .brand{font-size:4px;position:absolute;left:6px;top:13px}
.card .brand .dot{width:5px;height:5px}
.card.back{background:linear-gradient(135deg,var(--blue-light),var(--blue-dark))}
.card .info{position:absolute;left:4px;top:4px;font-size:2.6px;line-height:1.35;color:#fff}
.card .info b{font-size:3.4px;font-weight:600}
.card.white .info{color:var(--ink)}
.card.white .info b{color:var(--blue)}
.card.white .band{position:absolute;left:0;right:0;bottom:0;height:5px;background:var(--blue)}

/* letterhead */
.letter{width:160px;height:226px;top:11px}
.letter .brand{position:absolute;right:10px;top:12px;font-size:6px}
.letter .brand .dot{width:8px;height:8px}
.letter .body{position:absolute;left:14px;top:52px;width:130px;font-size:3.2px;line-height:1.9}
.letter .body p{margin-bottom:3px}
.letter .sign{width:30px;height:8px;background:linear-gradient(90deg,#cfd8e3,#eef2f6);margin:2px 0}
.letter .foot{position:absolute;left:14px;bottom:8px;font-size:2.8px;color:var(--muted)}
.letter svg{position:absolute;left:0;bottom:0}

/* slips and envelopes */
.slip{width:80px;height:38px}
.slip .brand{position:absolute;left:8px;top:10px;font-size:4.5px}
.slip .brand .dot{width:6px;height:6px}
.slip .note{position:absolute;left:8px;bottom:6px;font-size:3px;color:var(--muted)}
.slip.blue{background:linear-gradient(135deg,var(--blue-light),var(--blue-dark))}
.envelope{width:160px;height:60px}
.envelope .brand{position:absolute;left:10px;top:10px;font-size:5px}
.envelope .brand .dot{width:7px;height:7px}
.envelope .addr{position:absolute;left:10px;top:22px;font-size:3px;color:var(--muted);line-height:1.4}
.envelope svg{position:absolute;left:0;top:0}

/* folder */
.folder{left:965px;top:11px;width:225px;height:226px;background:linear-gradient(120deg,var(--blue-light),var(--blue) 45%,var(--blue-dark))}
.folder .fold{position:absolute;left:112px;top:0;bottom:0;width:1px;background:rgba(255,255,255,.35)}
.folder .brand{position:absolute;left:134px;top:40px;font-size:7px}
.folder .brand .dot{width:10px;height:10px}
.folder .pocket{position:absolute;left:0;right:113px;bottom:0;height:70px;background:linear-gradient(var(--blue),var(--blue-dark));border-top-right-radius:30px}
.folder .slot{position:absolute;left:60px;top:12px;width:44px;height:26px;background:var(--paper)}
.folder .slot .brand{position:absolute;left:4px;top:10px;font-size:3px;color:var(--blue)}
.folder .slot .brand .dot{width:4px;height:4px;background:var(--blue)}
.folder .web{position:absolute;right:14px;bottom:10px;font-size:3.5px;color:#fff}
</style>
</head>
<body>

<section class="intro">
  <div class="brand"><span class="dot"></span>Harlow Legal Partners</div>
  <div class="label">Business Cards</div>
</section>

<div class="piece card white" style="left:8px;top:96px">
  <div class="brand"><span class="dot"></span>Harlow Legal Partners</div>
  <div class="band"></div>
</div>
<div class="piece card back" style="left:70px;top:96px">
  <div class="info"><b>Derek M. Falbo</b><br>Trial Lawyer<br>2730 Birchwood Avenue<br>North Annex - Suite 2100<br>555-014-2737<br>derek@harlowcounsel.example</div>
</div>
<div class="piece card white" style="left:8px;top:150px">
  <div class="info"><b>Derek M. Falbo</b><br>Trial Lawyer<br>2730 Birchwood Avenue<br>North Annex - Suite 2100<br>Philadelphia, PA 19102<br>www.harlowcounsel.example</div>
  <div class="band"></div>
</div>
<div class="piece card back" style="left:70px;top:150px">
  <div class="brand light"><span class="dot"></span>Harlow Legal Partners</div>
</div>

<article class="piece letter" style="left:140px">
  <div class="brand"><span class="dot"></span>Harlow Legal Partners</div>
  <div class="body">
    <p>Dear Client,</p>
    <p>Thank you for choosing our firm. We review every case with care.</p>
    <p>Our trial team is ready to help. Please call us with any questions.</p>
    <p>Sincerely,</p>
    <div class="sign" role="img" aria-label="Handwritten signature"></div>
    <p>Derek M. Falbo</p>
  </div>
  <div class="foot">2730 Birchwood Avenue · 555-014-2737</div>
  <svg width="160" height="40" viewBox="0 0 160 40"><path d="M0 28 C50 10 110 42 160 18 V40 H0Z" fill="var(--blue-light)" opacity=".5"/><path d="M0 34 C60 20 110 44 160 28 V40 H0Z" fill="var(--blue)"/></svg>
</article>

<article class="piece letter" style="left:330px">
  <div class="brand"><span class="dot"></span>Harlow Legal Partners</div>
  <div class="body">
    <p>Dear Client,</p>
    <p>Thank you for choosing our firm. We review every case with care.</p>
    <p>Our trial team is ready to help. Please call us with any questions.</p>
    <p>Sincerely,</p>
    <div class="sign" role="img" aria-label="Handwritten signature"></div>
    <p>Derek M. Falbo</p>
  </div>
  <div class="foot">www.harlowcounsel.example</div>
  <svg width="160" height="40" viewBox="0 0 160 40"><path d="M0 28 C50 10 110 42 160 18 V40 H0Z" fill="var(--blue-light)" opacity=".5"/><path d="M0 34 C60 20 110 44 160 28 V40 H0Z" fill="var(--blue)"/></svg>
</article>

<div class="piece slip" style="left:555px;top:100px">
  <div class="brand"><span class="dot"></span>Harlow Legal Partners</div>
  <div class="note">With Compliments</div>
</div>
<div class="piece slip blue" style="left:650px;top:100px">
  <div class="brand light"><span class="dot"></span>Harlow Legal Partners</div>
</div>
<div class="piece slip" style="left:555px;top:150px">
  <div class="brand"><span class="dot"></span>Harlow Legal Partners</div>
  <div class="note">555-014-2737</div>
</div>
<div class="piece slip blue" style="left:650px;top:150px">
  <div class="brand light"><span class="dot"></span>Harlow Legal Partners</div>
</div>

<div class="piece envelope" style="left:785px;top:100px">
  <div class="brand"><span class="dot"></span>Harlow Legal Partners</div>
  <div class="addr">2730 Birchwood Avenue<br>North Annex - Suite 2100<br>Philadelphia, PA 19102</div>
</div>
<div class="piece envelope" style="left:785px;top:168px">
  <svg width="160" height="60" viewBox="0 0 160 60"><path d="M0 0 H160 L80 30Z" fill="var(--blue)"/><path d="M0 0 L80 30 L160 0" fill="none" stroke="var(--blue-dark)" stroke-width=".6"/></svg>
</div>

<div class="piece folder">
  <div class="fold"></div>
  <div class="brand light"><span class="dot"></span>Harlow Legal Partners</div>
  <div class="pocket">
    <div class="slot"><div class="brand"><span class="dot"></span>Harlow Legal Partners</div></div>
  </div>
  <div class="web">www.harlowcounsel.example</div>
</div>

</body>
</html>
```